Business Card Design

We Import cars and commercial vehicles, we have been in business around 12 years, we are based in Christchurch, New Zealand.
I really like the web address on card, possibly right along the bottom of the card?
We specialize in commercial vans, maybe worth a mention?
The logo has the name in it so probably don't need to have twice?

I really like a clean smart look, not too cluttered

Industry/Entity Type

Business

Contact Information for Business Card

RQL TOKYO IMPORTS, Derek Holloway, Managing Director
web address: www.rqlmotorsnz.com
cell phone. 021 485 912

Requirements
Must have
• the logo, and all the contact details.

Forgot to add my email address, derek@rqlmotorsnz.com
Nice to have
• Just thinking as the card is looking a little empty maybe somewhere written what we do? 'Specializing in commercial vans'
Not sure but we import Japanese vehicles, possibly adding some brands like Velkara Poremo Ketsu Brivon etc? Not sure on that one.

```html
<!DOCTYPE html>
<html lang="en">
<head>
<meta charset="utf-8">
<title>RQL Tokyo Imports – Business Card</title>
<link rel="stylesheet" href="https://fonts.googleapis.com/css2?family=Arimo:wght@400;700&display=swap">
<style>
  :root {
    --backdrop: #2b2b2b;
    --card: #ffffff;
    --ink: #111111;
    --ink-soft: #222222;
    --band: #0b0b0b;
    --silver-light: #f2f2f2;
    --silver-mid: #b9b9b9;
    --silver-dark: #6a6a6a;
    --badge: #c8c8c8;
    --van-light: #f4f4f4;
    --van-dark: #8d8d8d;
  }
  * { box-sizing: border-box; margin: 0; padding: 0; }
  html, body {
    width: 1200px; height: 743px; overflow: hidden;
    background: var(--backdrop);
    font-family: "Arimo", Arial, sans-serif;
    color: var(--ink);
  }
  .card {
    position: absolute; left: 160px; top: 101px;
    width: 880px; height: 540px;
    background: var(--card);
    border-radius: 28px;
    overflow: hidden;
  }
  .brand-name {
    position: absolute; left: 160px; top: 62px;
    font-weight: 700; color: var(--ink);
    line-height: 0.95; letter-spacing: 1px;
  }
  .brand-name .line-one { display: block; font-size: 52px; }
  .brand-name .line-two { display: block; font-size: 68px; }
  .van-illustration {
    position: absolute; left: 490px; top: 48px;
    width: 190px; height: 130px;
    border-radius: 14px;
    background: linear-gradient(160deg, var(--van-light), var(--van-dark));
  }
  .tagline {
    position: absolute; left: 196px; top: 186px;
    font-size: 15px; color: var(--ink-soft);
  }
  .person {
    position: absolute; right: 460px; top: 246px;
    text-align center;
    text-align: center;
  }
  .person-name { font-size: 32px; font-weight: 700; line-height: 1.1; }
  .person-title { font-size: 20px; margin-top: 2px; }
  .divider {
    position: absolute; left: 440px; top: 244px;
    width: 2px; height: 66px; background: var(--ink-soft);
  }
  .contact {
    position: absolute; left: 468px; top: 246px;
    list-style: none;
    font-size: 18px; font-weight: 700;
  }
  .contact li { display: flex; align-items: center; gap: 14px; height: 30px; }
  .contact svg { width: 18px; height: 18px; fill: var(--ink); }
  .makes {
    position: absolute; left: 0; right: 0; top: 344px;
    display: flex; justify-content: center; gap: 36px;
  }
  .make {
    display: flex; flex-direction: column; align-items: center; gap: 6px;
    font-size: 13px; font-weight: 700; color: var(--ink-soft);
    text-transform: uppercase;
  }
  .make-badge {
    width: 32px; height: 32px; border-radius: 50%; background: var(--badge);
  }
  .footer-band {
    position: absolute; left: 0; top: 428px;
    width: 100%; height: 112px; background: var(--band);
  }
  .web-strip {
    position: absolute; left: 0; top: 462px;
    width: 100%; height: 42px;
    background: linear-gradient(90deg, var(--silver-dark), var(--silver-light) 35%, var(--silver-mid) 65%, var(--silver-dark));
    display: flex; align-items: center; justify-content: center; gap: 12px;
    font-size: 18px; font-weight: 700; color: var(--ink);
  }
  .web-strip svg { width: 22px; height: 22px; }
</style>
</head>
<body>
  <main class="card">
    <h1 class="brand-name">
      <span class="line-one">RQL TOKYO</span>
      <span class="line-two">IMPORTS</span>
    </h1>
    <div class="van-illustration" role="img" aria-label="Illustration of a white commercial van"></div>
    <p class="tagline">Specializing in commercial vans</p>

    <div class="person">
      <p class="person-name">Derek Holloway</p>
      <p class="person-title">Managing Director</p>
    </div>
    <div class="divider"></div>
    <ul class="contact">
      <li>
        <svg viewBox="0 0 18 18" aria-hidden="true"><path d="M5 1h8a1.5 1.5 0 0 1 1.5 1.5v13A1.5 1.5 0 0 1 13 17H5a1.5 1.5 0 0 1-1.5-1.5v-13A1.5 1.5 0 0 1 5 1zm0 2v10h8V3zm4 11a1 1 0 1 0 0 2 1 1 0 0 0 0-2z" fill-rule="evenodd"/></svg>
        021 485 912
      </li>
      <li>
        <svg viewBox="0 0 18 18" aria-hidden="true"><path d="M1 4h16v10H1zm1.5 1.2L9 10l6.5-4.8V5h-13z"/></svg>
        derek@rqlmotorsnz.com
      </li>
    </ul>

    <div class="makes">
      <div class="make"><span class="make-badge"></span>Velkara</div>
      <div class="make"><span class="make-badge"></span>Ketsu</div>
      <div class="make"><span class="make-badge"></span>Poremo</div>
      <div class="make"><span class="make-badge"></span>Brivon</div>
    </div>

    <div class="footer-band"></div>
    <div class="web-strip">
      <svg viewBox="0 0 22 22" aria-hidden="true" fill="none" stroke="#111" stroke-width="1.6">
        <circle cx="11" cy="11" r="9.5" fill="#111"/>
        <g stroke="#ddd" stroke-width="1.2">
          <line x1="2" y1="11" x2="20" y2="11"/>
          <line x1="11" y1="2" x2="11" y2="20"/>
          <line x1="3.5" y1="6.5" x2="18.5" y2="6.5"/>
          <line x1="3.5" y1="15.5" x2="18.5" y2="15.5"/>
          <line x1="6.5" y1="3.5" x2="6.5" y2="18.5"/>
          <line x1="15.5" y1="3.5" x2="15.5" y2="18.5"/>
        </g>
      </svg>
      www.rqlmotorsnz.com
    </div>
  </main>
</body>
</html>
```